New Business Card Design Project

Need a design that will create an impact / strong impression towards our clients for our business. We are in the lighting business and we do lighting retrofits for large commercial to industrial clientele.

Target Market(s)

Lighting Industry

Industry/Entity Type

Business

Font styles to use
Other font styles liked:
• we would like to use the font on our logo, not sure what it is though..

Requirements
Must have
• Our logo.
Nice to have
• We are open to suggestions that have to do with lighting.

```html
<!DOCTYPE html>
<html lang="en">
<head>
<meta charset="utf-8">
<title>Lumena Retrofit Co. – Business Card</title>
<link rel="stylesheet" href="https://fonts.googleapis.com/css2?family=Lato:wght@400;700&family=Montserrat:wght@400;700&display=swap">
<style>
  :root {
    --backdrop: #e7e1d8;
    --card: #f1eee9;
    --card-edge: #ffffff;
    --green: #3f9a3c;
    --green-dark: #1f5e2b;
    --text-grey: #6f6b66;
  }
  html, body {
    margin: 0;
    width: 1200px;
    height: 1047px;
    overflow: hidden;
    background: var(--backdrop);
  }
  .card {
    position: absolute;
    left: 100px;
    top: 251px;
    width: 1000px;
    height: 545px;
    background: var(--card);
    border: 2px solid var(--card-edge);
    border-radius: 26px;
    box-sizing: border-box;
    font-family: "Lato", sans-serif;
  }
  .holder { position: absolute; left: 44px; top: 60px; }
  .holder-name {
    margin: 0;
    font-size: 30px;
    font-weight: 700;
    letter-spacing: 0.5px;
    color: var(--green);
  }
  .holder-role {
    margin: 2px 0 0;
    font-size: 23px;
    color: var(--text-grey);
  }
  .brand {
    position: absolute;
    right: 44px;
    top: 82px;
    text-align: right;
    color: var(--green-dark);
    font-family: "Lato", sans-serif;
    font-weight: 700;
  }
  .brand-name { display: block; font-size: 62px; line-height: 1; letter-spacing: 2px; }
  .brand-sub { display: block; font-size: 17px; letter-spacing: 1.5px; margin-top: 8px; }
  .address {
    position: absolute;
    left: 44px;
    top: 280px;
    margin: 0;
    font-family: "Montserrat", sans-serif;
    font-size: 19px;
    line-height: 34px;
    color: var(--text-grey);
    font-style: normal;
  }
  .contacts {
    position: absolute;
    left: 44px;
    top: 410px;
    margin: 0;
    padding: 0;
    list-style: none;
    font-family: "Montserrat", sans-serif;
    font-size: 19px;
    color: var(--text-grey);
    letter-spacing: 0.5px;
  }
  .contacts li { display: flex; align-items: center; height: 31px; }
  .contacts svg { width: 16px; height: 16px; margin-right: 22px; fill: var(--green-dark); }
</style>
</head>
<body>
  <div class="card">
    <div class="holder">
      <h1 class="holder-name">DANIEL REYES</h1>
      <p class="holder-role">Founder</p>
    </div>

    <div class="brand">
      <span class="brand-name">LUMENA</span>
      <span class="brand-sub">LUMENA RETROFIT CO.</span>
    </div>

    <address class="address">
      4870 Meridian Avenue,<br>
      Suite Tucson 85712
    </address>

    <ul class="contacts">
      <li>
        <svg viewBox="0 0 16 16" aria-hidden="true"><path d="M3.2 1.2 5.6 1l1.3 3.4-1.6 1.2a9 9 0 0 0 5 5l1.2-1.6 3.4 1.3-.2 2.4c-.1.7-.7 1.2-1.4 1.2C6.5 13.7 2.3 9.5 2 2.6c0-.7.5-1.3 1.2-1.4z"/></svg>
        0400 555 019
      </li>
      <li>
        <svg viewBox="0 0 16 16" aria-hidden="true"><path d="M1 3h14v1.6L8 9 1 4.6z"/><path d="M1 6.4 8 10.8l7-4.4V13H1z"/></svg>
        info@lumenaretrofit.com
      </li>
      <li>
        <svg viewBox="0 0 16 16" aria-hidden="true"><circle cx="8" cy="8" r="7"/><path d="M1 8h14M8 1c2.5 2.5 2.5 11.5 0 14M8 1C5.5 3.5 5.5 12.5 8 15" stroke="#f1eee9" stroke-width="1.1" fill="none"/></svg>
        www.lumenaretrofit.com
      </li>
    </ul>
  </div>
</body>
</html>
```